we need a pizza box design for the 12 inch pizza consist of the 3 color no specific color for the logo or for the design the box is the same shape of the farrow pizza box attached i need to write few things like : hot s& delicious and Fall in Love with Pizza
adress on the box K29 Olutemi bakare road kubwa abuja
tel.: 0703 61 284 97
i might add the pizza name with check box
for example
margarita O
Tamblins pizza
Vexa Pizza
seafood Pizza
other --------------
with check box next to it i have 8 type of pizza

Target Market(s)

its a pizza box people are buying it anyway

Industry/Entity Type

Restaurant

Font styles to use
Serif
Decorative
Script

Colors
abd037
eaf2ce
9ccb3b

Requirements
Must have
• simple and elegant
• with real carton color not white
Nice to have
• new creative idea
Should not have
• no pork or bacon

```html
<!DOCTYPE html>
<html lang="en">
<head>
<meta charset="utf-8">
<title>Marlow Crust Cafe – Pizza Box</title>
<link rel="stylesheet" href="https://fonts.googleapis.com/css2?family=Cinzel:wght@500&family=Lobster&family=Oswald:wght@600&family=Roboto:wght@400&display=swap">
<style>
  :root {
    --lime: #abd037;
    --lime-mid: #9ccb3b;
    --pale: #eaf2ce;
    --ink: #4a7418;
    --paper: #fbfcf6;
    --backdrop: #2b2621;
  }
  * { box-sizing: border-box; margin: 0; padding: 0; }
  html, body { width: 1200px; height: 900px; overflow: hidden; background: var(--backdrop); }
  .canvas { position: relative; width: 1200px; height: 900px; }

  .band {
    position: absolute; background: var(--lime);
    display: flex; align-items: center; justify-content: center;
    color: var(--ink);
  }
  .band--top { left: 320px; top: 80px; width: 560px; height: 90px; justify-content: space-between; padding: 0 28px; }
  .band--bottom { left: 320px; top: 730px; width: 560px; height: 90px; }
  .band--left { left: 230px; top: 170px; width: 90px; height: 560px; }
  .band--right { left: 880px; top: 170px; width: 90px; height: 560px; }

  .slogan { font-family: "Lobster", cursive; font-size: 44px; letter-spacing: .5px; }
  .slogan--small { font-size: 34px; }

  .menu-list { list-style: none; font-family: "Lobster", cursive; font-size: 15px; line-height: 19px; }
  .menu-list li { display: flex; align-items: center; justify-content: flex-end; gap: 8px; }
  .check { width: 13px; height: 13px; border: 1.5px solid var(--ink); display: inline-flex; }
  .check svg { width: 100%; height: 100%; }

  .vertical { display: flex; align-items: center; gap: 16px; white-space: nowrap; }
  .vertical--left { transform: rotate(-90deg); }
  .vertical--right { transform: rotate(90deg); }
  .phone { font-family: "Oswald", sans-serif; font-size: 40px; letter-spacing: 1px; }
  .address { font-family: "Roboto", sans-serif; font-size: 14px; line-height: 17px; display: flex; align-items: center; gap: 6px; }
  .address svg { width: 14px; height: 18px; flex: none; }

  .mini-mark {
    width: 56px; height: 56px; border: 2px solid var(--ink); background: var(--pale);
    display: flex; align-items: center; justify-content: center; text-align: center;
    font-family: "Cinzel", serif; font-size: 9px; line-height: 11px; color: var(--ink);
  }

  .lid {
    position: absolute; left: 320px; top: 170px; width: 560px; height: 560px;
    background: var(--paper);
  }
  .lid__art {
    position: absolute; inset: 0;
    background: radial-gradient(circle at 50% 50%, var(--paper) 0%, var(--pale) 100%);
  }
  .brand-panel {
    position: absolute; left: 170px; top: 170px; width: 220px; height: 220px;
    background: linear-gradient(160deg, #ffffff 0%, var(--pale) 100%);
    border: 5px solid var(--lime-mid); outline: 10px solid rgba(234,242,206,.9);
    display: flex; flex-direction: column; align-items: center; justify-content: center; gap: 12px;
  }
  .brand-panel__dot { width: 18px; height: 18px; border-radius: 50%; background: var(--ink); }
  .brand-name {
    font-family: "Cinzel", serif; font-size: 30px; line-height: 36px; color: var(--ink);
    text-align: center; letter-spacing: 3px;
  }
</style>
</head>
<body>
<main class="canvas">

  <section class="band band--top" aria-label="Menu side">
    <div class="mini-mark">Marlow Crust Cafe</div>
    <span class="slogan">Hot &amp; Delicious</span>
    <ul class="menu-list">
      <li>Margarita O <span class="check"><svg viewBox="0 0 10 10"><path d="M2 5.5 L4.2 7.8 L8.5 2" fill="none" stroke="#4a7418" stroke-width="1.6"/></svg></span></li>
      <li>Tamblins pizza <span class="check"></span></li>
      <li>Vexa Pizza <span class="check"></span></li>
      <li>Seafood Pizza <span class="check"></span></li>
    </ul>
  </section>

  <section class="band band--left" aria-label="Phone side">
    <div class="vertical vertical--left">
      <span class="phone">0703-61-284-97</span>
    </div>
  </section>

  <section class="band band--right" aria-label="Address side">
    <div class="vertical vertical--right">
      <span class="address">
        <svg viewBox="0 0 14 18"><path d="M7 1a5.5 5.5 0 0 0-5.5 5.5C1.5 11 7 17 7 17s5.5-6 5.5-10.5A5.5 5.5 0 0 0 7 1z" fill="none" stroke="#4a7418" stroke-width="1.6"/><circle cx="7" cy="6.5" r="2" fill="#4a7418"/></svg>
        K29 Olutemi bakare road<br>kubwa abuja
      </span>
      <div class="mini-mark">Marlow Crust Cafe</div>
    </div>
  </section>

  <section class="band band--bottom" aria-label="Slogan side">
    <span class="slogan slogan--small">Fall in Love with Pizza</span>
  </section>

  <section class="lid">
    <div class="lid__art" role="img" aria-label="Green hand-drawn line art of pizza slices, forks, knives, peppers, olives and basil leaves covering the lid"></div>
    <div class="brand-panel">
      <span class="brand-panel__dot"></span>
      <h1 class="brand-name">Marlow<br>Crust Cafe</h1>
    </div>
  </section>

</main>
</body>
</html>
```